Ostrander Granite Hall Museum Website (Design Only)

The Ostrander Granite Hall is a newly renovated historical building in lower Manhattan. We are building a website for them so that tours and events can be scheduled. We have provided typography requirements along with many photographs. You are free to be creative with the use of the photographs in your design. There is no specific brand or color guidelines but the client did specify that they wanted the website to be clean, simple and elegant BUT to also reflect the vintage colors and feeling of the building. Please do NOT design the logo as we have a separate contest for the logo. We have provided a mock up of all website pages that we would like designed. however we encourage you to design and submit the home page an a few other pages first so we can provide feedback. The designs that you provide must be compatible with Wix.

```html
<!DOCTYPE html>
<html lang="en">
<head>
<meta charset="utf-8">
<title>Ostrander Granite Hall</title>
<link href="https://fonts.googleapis.com/css2?family=Jost:wght@300;400;500;600;700&family=IBM+Plex+Sans:wght@400;500&family=Titillium+Web:wght@600;700&display=swap" rel="stylesheet">
<style>
  :root {
    --paper: #efe6d2;
    --paper-light: #f4ecdc;
    --green: #93c47d;
    --ink: #262626;
    --text: #3b3b3b;
    --white: #ffffff;
    --footer: #1d1d1d;
  }
  * { margin: 0; padding: 0; box-sizing: border-box; }
  html, body { width: 1121px; height: 1200px; overflow: hidden; }
  body {
    position: relative;
    background: radial-gradient(ellipse at 50% 30%, var(--paper-light), var(--paper) 70%);
    font-family: "IBM Plex Sans", sans-serif;
    color: var(--text);
  }
  .brand {
    position: absolute; left: 105px; top: 16px;
    display: flex; align-items: center; gap: 10px;
  }
  .brand-mark { width: 92px; height: 92px; background: #3a2a1e; }
  .brand-name {
    font-family: "Jost", sans-serif; font-weight: 400;
    font-size: 25px; line-height: 31px; color: var(--ink);
  }
  .contact-bar {
    position: absolute; left: 358px; top: 0; width: 763px; height: 56px;
    background: var(--green); color: var(--white);
    display: flex; align-items: center; padding-left: 26px;
    font-size: 16px; gap: 12px;
  }
  .contact-bar b { font-weight: 500; }
  .contact-item { display: flex; align-items: center; gap: 10px; }
  .divider { opacity: .9; margin: 0 2px; }
  .social { width: 35px; height: 35px; border-radius: 50%; background: var(--white); }
  .main-nav {
    position: absolute; left: 369px; top: 93px;
    display: flex; gap: 22px; font-size: 14px; color: var(--ink);
  }
  .hero-title {
    position: absolute; top: 155px; left: 0; width: 1121px; text-align: center;
    font-family: "Jost", sans-serif; font-weight: 300; font-size: 47px; color: var(--ink);
  }
  .hero-title strong { font-weight: 600; color: var(--green); }
  .hero-text {
    position: absolute; top: 243px; left: 0; width: 1121px; text-align: center;
    font-size: 14.5px; line-height: 28px; color: var(--ink);
  }
  .skyline {
    position: absolute; top: 320px; left: 0; width: 1121px; height: 365px;
    background: linear-gradient(180deg, #e9e1cf 0%, #bdb8ad 30%, #8c8a84 55%, #6f6a60 78%, #44587a 88%, #3a4e6e 100%);
  }
  .cards { position: absolute; top: 719px; left: 105px; display: flex; gap: 41px; }
  .card {
    width: 277px; height: 354px; background: var(--white);
    box-shadow: 0 2px 12px rgba(0,0,0,.12); text-align: center;
  }
  .card-photo { height: 184px; }
  .photo-hours { background: linear-gradient(160deg, #5b88c4, #a9b6c4 35%, #4a4533 70%, #3b3526); }
  .photo-see { background: linear-gradient(180deg, #3f94d8, #b9d9ef 45%, #5a513a 62%, #2e2a20); }
  .photo-history { background: linear-gradient(90deg, #3d2a22 0%, #4a3228 22%, #c9b98b 38%, #d4c293 62%, #4a3228 78%, #3d2a22); }
  .card-title {
    margin-top: 18px; font-family: "Jost", sans-serif; font-weight: 600;
    font-size: 21px; letter-spacing: .3px; color: var(--ink);
  }
  .card-text { margin-top: 9px; font-size: 14px; line-height: 24px; height: 48px; }
  .btn {
    margin: 17px auto 0; width: 178px; height: 32px; background: var(--green);
    color: var(--white); font-family: "Titillium Web", sans-serif; font-weight: 700;
    font-size: 10px; display: flex; align-items: center; justify-content: center; gap: 8px;
  }
  .site-footer {
    position: absolute; left: 0; top: 1119px; width: 1121px; height: 81px;
    background: var(--footer); color: var(--white);
    display: flex; align-items: center; justify-content: center; font-size: 13px; gap: 10px;
  }
</style>
</head>
<body>
  <header>
    <div class="brand">
      <div class="brand-mark"></div>
      <div class="brand-name">Ostrander<br>Granite<br>Hall</div>
    </div>
    <div class="contact-bar">
      <span class="contact-item">
        <svg width="16" height="16" viewBox="0 0 24 24"><path fill="#fff" d="M6.6 10.8a15.1 15.1 0 0 0 6.6 6.6l2.2-2.2a1 1 0 0 1 1-.25 11.4 11.4 0 0 0 3.6.57 1 1 0 0 1 1 1V20a1 1 0 0 1-1 1A17 17 0 0 1 3 4a1 1 0 0 1 1-1h3.5a1 1 0 0 1 1 1c0 1.25.2 2.45.57 3.57a1 1 0 0 1-.25 1z"/></svg>
        <span><b>Phone :</b> +1 (555) 010 2040</span>
      </span>
      <span class="divider">|</span>
      <span class="contact-item">
        <svg width="18" height="14" viewBox="0 0 18 14"><rect width="18" height="14" rx="1.5" fill="#fff"/><path d="M1 1.5l8 6 8-6" stroke="#93c47d" stroke-width="1.6" fill="none"/></svg>
        <span><b>Email :</b> info@ostrandergranitehall.com</span>
      </span>
      <span class="divider">|</span>
      <span class="social"></span>
      <span class="social"></span>
    </div>
    <nav class="main-nav">
      <span>About the Building</span><span>Calendar</span><span>Public Exhibitions</span><span>Tour the Building</span><span>Plan Your Visit</span><span>Contact Us</span>
    </nav>
  </header>

  <main>
    <h1 class="hero-title">Welcome to the <strong>Ostrander Granite Hall</strong></h1>
    <p class="hero-text">The majestic Ostrander Granite Hall stands beside the old harbor downtown. Built of carved granite, the building<br>is a treasured historic landmark that welcomes visitors all year round.</p>
    <div class="skyline" role="img" aria-label="Photograph of a city skyline with the hall on the waterfront"></div>

    <section class="cards">
      <article class="card">
        <div class="card-photo photo-hours" role="img" aria-label="Photograph of the ornate facade seen from below against a cloudy sky"></div>
        <h2 class="card-title">HOURS</h2>
        <p class="card-text">Check the calendar to see our<br>hours of operation.</p>
        <div class="btn">
          <svg width="14" height="14" viewBox="0 0 14 14" fill="none" stroke="#fff" stroke-width="1.2"><rect x="1" y="2.5" width="12" height="10.5"/><path d="M1 5.5h12M4 1v3M10 1v3M4 8h1M7 8h1M10 8h1M4 10.5h1M7 10.5h1"/></svg>
          GO TO CALENDAR
        </div>
      </article>
      <article class="card">
        <div class="card-photo photo-see" role="img" aria-label="Photograph of the building front under a blue sky"></div>
        <h2 class="card-title">WHAT TO SEE</h2>
        <p class="card-text">Our building hosts<br>exhibitions of all kinds.</p>
        <div class="btn">
          <svg width="18" height="13" viewBox="0 0 18 13" fill="none" stroke="#fff" stroke-width="1.2"><rect x="1" y="1" width="16" height="11"/><rect x="3" y="3" width="12" height="7"/><path d="M3 10l4-4 3 3 2-2 3 3"/></svg>
          EXHIBITIONS
        </div>
      </article>
      <article class="card">
        <div class="card-photo photo-history" role="img" aria-label="Photograph of historic wooden doors with decorative glass panels"></div>
        <h2 class="card-title">HISTORY</h2>
        <p class="card-text">A building of the city’s proud<br>maritime history.</p>
        <div class="btn">
          <svg width="16" height="16" viewBox="0 0 16 16" fill="none" stroke="#fff" stroke-width="1.2"><circle cx="8" cy="8" r="7"/><circle cx="8" cy="8" r="4.5"/><circle cx="8" cy="8" r="2"/><path d="M8 8l6-6"/></svg>
          OUR MISSION
        </div>
      </article>
    </section>
  </main>

  <footer class="site-footer">
    <span>©Copyrights 2022 Ostrander Granite Hall</span><span>|</span><span>All Rights Reserved</span>
  </footer>
</body>
</html>
```